Business Card Design Project - bel soravin group

dear Sirs

we need business card design for our group ( BEL Soravin Group ) , i have got the Logo design of our group from pixel harbor in previous , so all need details relating to our group i think available with you, as well as the the chosen logo design

we hope to provide us with business card logo that to be appropaite and satisfactory to us .

thanks

note : logo design of our group is attached .
Updates

Reason: please extend the deadline of my project for additional 15 days because i didn't received appropriate design for our gruop yet . kindly beaware that i have received 77 design till now , supossed to send me 200-250 design at least . thanks

Target Market(s)

contents
-

name : Korvan EL Mistrani

position : Operation Manager

Industry/Entity Type

Business

Requirements
Must have

• person name

group logo
Nice to have
• logo color matching with back background

```html
<!DOCTYPE html>
<html lang="en">
<head>
<meta charset="utf-8">
<title>BEL Soravin Group – Business Card</title>
<link rel="stylesheet" href="https://fonts.googleapis.com/css2?family=Source+Sans+3:wght@400;600;700&display=swap">
<style>
  :root {
    --page: #ffffff;
    --card-black: #0b0b0c;
    --card-white: #ffffff;
    --brand-blue: #1a5a9c;
    --gold: #c9a645;
    --gold-light: #e3c777;
    --text-light: #f2f2f2;
    --shadow: rgba(0,0,0,0.35);
  }
  * { box-sizing: border-box; margin: 0; padding: 0; }
  html, body {
    width: 1200px; height: 900px; overflow: hidden;
    background: var(--page);
    font-family: "Source Sans 3", "Myriad Pro", Arial, sans-serif;
  }
  .canvas { position: relative; width: 1200px; height: 900px; }

  .card {
    position: absolute; left: 305px; width: 627px; height: 360px;
    box-shadow: 6px 8px 10px var(--shadow);
    overflow: hidden;
  }
  .card--front { top: 57px; background: var(--card-black); }
  .card--back { top: 471px; background: var(--card-black); }

  /* Front */
  .front-top {
    position: absolute; left: 0; top: 0; width: 100%; height: 192px;
    background: var(--card-white);
    display: flex; align-items: center; justify-content: center;
  }
  .gold-rule {
    position: absolute; left: 0; top: 192px; width: 100%; height: 9px;
    background: var(--gold);
  }
  .brand-name {
    display: flex; align-items: center; gap: 14px;
    color: var(--brand-blue); font-weight: 600; font-size: 46px;
    letter-spacing: 1px; white-space: nowrap; line-height: 1;
  }
  .brand-name .brand-mark {
    width: 20px; height: 20px; background: var(--brand-blue); flex: none;
  }

  .contact {
    position: absolute; left: 40px; top: 228px;
    color: var(--text-light); font-size: 15.5px; line-height: 22px;
    list-style: none;
  }
  .contact li { display: flex; align-items: center; gap: 8px; }
  .contact .address { margin-bottom: 2px; }
  .contact svg { width: 13px; height: 13px; fill: var(--brand-blue); flex: none; }

  .person {
    position: absolute; right: 42px; top: 243px; text-align: right;
  }
  .person .name {
    color: var(--gold); font-weight: 700; font-size: 22px; line-height: 28px;
  }
  .person .role {
    color: var(--text-light); font-size: 15.5px; line-height: 22px;
  }

  .web-band {
    position: absolute; right: 0; top: 331px; width: 281px; height: 29px;
  }
  .web-band svg { position: absolute; inset: 0; width: 100%; height: 100%; }
  .web-band .url {
    position: absolute; right: 42px; top: 4px;
    color: var(--card-white); font-size: 15.5px; line-height: 20px;
  }

  /* Back */
  .back-brand {
    position: absolute; left: 0; top: 160px; width: 100%;
    display: flex; justify-content: center;
  }
  .back-url {
    position: absolute; left: 0; top: 296px; width: 100%; text-align: center;
    color: var(--text-light); font-size: 19px;
  }
</style>
</head>
<body>
<main class="canvas">

  <section class="card card--front" aria-label="Business card front">
    <div class="front-top">
      <div class="brand-name"><span class="brand-mark"></span>BEL SORAVIN GROUP</div>
    </div>
    <div class="gold-rule"></div>

    <ul class="contact">
      <li class="address">P.O. Box 418, Marlow Heath, Vic, 3192</li>
      <li>
        <svg viewBox="0 0 16 16" aria-hidden="true"><path d="M3.5 1l2.5 3-1.5 2c1 2 3 4 5 5l2-1.5 3 2.5-1.5 2.5C8 16 0 8 1.5 2.5z"/></svg>
        02 7391 4406
      </li>
      <li>
        <svg viewBox="0 0 16 16" aria-hidden="true"><path d="M4 1h8v4H4zM1 6h14v7h-3v2H4v-2H1zM5 10v4h6v-4z"/></svg>
        02 7391 4406
      </li>
      <li>
        <svg viewBox="0 0 16 16" aria-hidden="true"><path d="M4 0h8a1 1 0 011 1v14a1 1 0 01-1 1H4a1 1 0 01-1-1V1a1 1 0 011-1zm1 2v10h6V2zm3 11a1 1 0 100 2 1 1 0 000-2z"/></svg>
        02 7391 4406
      </li>
      <li>
        <svg viewBox="0 0 16 16" aria-hidden="true"><path d="M0 3h16v10H0zm1 1l7 5 7-5z" fill-rule="evenodd"/></svg>
        korvan@belsoravin.com
      </li>
    </ul>

    <div class="person">
      <p class="name">Korvan EL Mistrani</p>
      <p class="role">Operation Manager</p>
    </div>

    <div class="web-band">
      <svg viewBox="0 0 281 29" preserveAspectRatio="none" aria-hidden="true">
        <polygon points="0,29 22,0 34,0 12,29" fill="var(--gold-light)"/>
        <polygon points="16,29 38,0 281,0 281,29" fill="var(--gold)"/>
      </svg>
      <span class="url">www.belsoravin.com</span>
    </div>
  </section>

  <section class="card card--back" aria-label="Business card back">
    <div class="back-brand">
      <div class="brand-name"><span class="brand-mark"></span>BEL SORAVIN GROUP</div>
    </div>
    <p class="back-url">www.belsoravin.com</p>
  </section>

</main>
</body>
</html>
```